Downtown hair salon need trendy website

I need a website with style. Unique. We need this site to list prices , Hair and nail services, service providers hours. I would also like my logo design on the website. We are located Midtown Harbor Falls. Beautiful city with lots of culture.

Target Market(s)

Men and women

Industry/Entity Type

Hair And Beauty

Coding

Coded - Design and coding required

Number of Pages Required

3 page

Font styles to use
Sans Serif

Colors

Designer to choose colors to be used in the design.

Requirements
Must have
• Logo of business. Hours, services and prices, Page for pictures of each service provider. Nail service and prices. Products that we carry... Area on page for my mission statement.
Nice to have
• Pictures of trendy of the beauty industry. Men and women cuts.. Nails..
Should not have
• booking on line options...

```html
<!DOCTYPE html>
<html lang="en">
<head>
<meta charset="utf-8">
<title>Tressera Midtown – Hair &amp; Nail Salon</title>
<link href="https://fonts.googleapis.com/css2?family=Playfair+Display:wght@400;700;900&family=Poppins:wght@300;400;500;600&family=Open+Sans:wght@400;600&display=swap" rel="stylesheet">
<style>
:root{
  --orange:#f47a2c;
  --orange-soft:#f89a52;
  --yellow:#fcc62a;
  --ink:#1c1c1c;
  --text:#555;
  --muted:#999;
  --line:#e6e6e6;
  --grey-bg:#f4f4f4;
  --white:#fff;
  --gold:#c99a3b;
  --cream:#fffde8;
  --mint:#eafdea;
  --blush:#fdeaea;
  --ice:#e8fbfb;
}
*{box-sizing:border-box;margin:0;padding:0}
html,body{width:1200px;height:3700px;overflow:hidden;background:var(--white)}
body{position:relative;font-family:'Poppins',sans-serif;color:var(--ink)}
.abs{position:absolute}
.serif{font-family:'Playfair Display',serif}
.small{font-family:'Open Sans',sans-serif;font-size:9px;line-height:15px;color:var(--text)}
.btn{position:absolute;display:flex;align-items:center;justify-content:center;border-radius:30px;font-size:9px;letter-spacing:2px;font-weight:600;text-transform:uppercase}
.btn-orange{background:var(--orange);color:var(--white)}
.btn-yellow{background:var(--yellow);color:var(--ink)}
.photo{position:absolute}

/* header */
.brand{left:75px;top:0;width:170px;height:70px;background:var(--white);display:flex;align-items:center;justify-content:center;gap:8px;z-index:3}
.brand-mark{width:10px;height:10px;background:var(--gold)}
.brand-name{font-family:'Poppins',sans-serif;font-size:17px;font-weight:500;color:var(--gold);letter-spacing:1px}
.nav{left:244px;top:0;width:390px;height:70px;background:var(--white);display:flex;align-items:center;justify-content:center;gap:10px;font-size:9px;font-weight:500;letter-spacing:1px;z-index:3}
.nav .dot{color:var(--muted)}
.nav .on{font-weight:600;border-bottom:1px solid var(--ink)}
.locbar{left:634px;top:0;width:403px;height:70px;background:var(--white);z-index:3}
.contact-box{left:1037px;top:0;width:163px;height:70px;background:var(--orange);color:var(--white);font-size:10px;letter-spacing:2px;display:flex;align-items:center;justify-content:center;gap:8px;z-index:3}
.pager{left:0;top:220px;width:50px}
.pager div{font-size:8px;color:var(--muted);height:44px;display:flex;align-items:center;gap:6px}
.pager .cur{color:var(--ink)}
.pager .cur:before{content:"";width:20px;height:1px;background:var(--ink)}
.pager div:not(.cur){padding-left:26px}

/* about */
.h-serif{font-family:'Playfair Display',serif;font-weight:700;font-size:21px;line-height:24px}
.h-sub{font-size:14px;font-weight:400;line-height:18px}

/* styles grid */
.grid{left:234px;top:1594px;width:732px;height:376px;display:grid;grid-template-columns:repeat(4,183px);grid-template-rows:repeat(2,188px)}
.cell{padding:30px 20px}
.cell h3{font-family:'Playfair Display',serif;font-size:21px;font-weight:700;line-height:22px}
.cell .kind{font-size:14px;line-height:18px}
.cell .at{font-size:7px;color:var(--muted);margin-top:8px}
.cell .price{font-size:18px;font-weight:500;margin-top:22px}

/* services */
.svc{position:absolute;top:2808px;width:160px;text-align:center}
.ring{width:112px;height:112px;border-radius:50%;border:1.5px solid var(--ink);margin:0 auto;display:flex;align-items:center;justify-content:center}
.ring.fill{background:var(--yellow);border-color:var(--yellow)}
.slash{color:var(--gold);font-size:12px;margin-top:12px}
.svc h4{font-family:'Playfair Display',serif;font-size:15px;font-weight:700;margin-top:6px}

/* footer */
.f-head{font-family:'Playfair Display',serif;font-weight:700;font-size:15px;line-height:17px}
.hours{font-size:8px;color:var(--text);line-height:19.5px}
.hours td{padding-right:40px}
</style>
</head>
<body>

<!-- HEADER / HERO -->
<div class="abs brand"><span class="brand-mark"></span><span class="brand-name">TRESSERA</span></div>
<nav class="abs nav"><span class="on">HOME</span><span class="dot">•</span><span>HAIR &amp; NAIL SERVICES</span><span class="dot">•</span><span>MEN</span><span class="dot">•</span><span>WOMEN</span><span class="dot">•</span><span>CONTACT</span></nav>
<div class="abs locbar">
  <svg class="abs" style="left:50px;top:23px" width="26" height="26" viewBox="0 0 26 26"><circle cx="13" cy="13" r="12" fill="none" stroke="#f47a2c"/><path d="M13 7a4 4 0 0 0-4 4c0 3 4 8 4 8s4-5 4-8a4 4 0 0 0-4-4z" fill="none" stroke="#f47a2c"/><circle cx="13" cy="11" r="1.3" fill="#f47a2c"/></svg>
  <div class="abs" style="left:90px;top:15px;font-size:7px;color:var(--muted);letter-spacing:1px">WE ARE LOCATED</div>
  <div class="abs serif" style="left:90px;top:28px;font-size:8px;line-height:9px">418 Cedar Lane Suite 3<br>Harbor Falls, MI 49010<br>555-014-2290</div>
  <svg class="abs" style="left:265px;top:30px" width="70" height="12" viewBox="0 0 70 12"><circle cx="6" cy="6" r="5" fill="#f47a2c"/><rect x="27" y="1" width="10" height="10" rx="2" fill="#f47a2c"/><circle cx="60" cy="6" r="5" fill="none" stroke="#f47a2c" stroke-width="1.5"/></svg>
</div>
<div class="abs contact-box"><svg width="14" height="10" viewBox="0 0 14 10"><rect x=".5" y=".5" width="13" height="9" fill="none" stroke="#fff"/><path d="M.5.5 7 6 13.5.5" fill="none" stroke="#fff"/></svg>CONTACT US</div>
<div class="abs pager"><div class="cur">01</div><div>02</div><div>03</div></div>

<div class="photo" role="img" aria-label="Blurred salon interior" style="left:75px;top:70px;width:169px;height:444px;background:linear-gradient(160deg,#e8dccf,#c9ab8e 60%,#efe6dc)"></div>
<div class="photo" role="img" aria-label="Smiling woman with curly hair in a striped top" style="left:244px;top:0;width:390px;height:514px;background:linear-gradient(180deg,#efe2d2,#d9b79a 45%,#b5616a 75%,#e3a86e)"></div>
<div class="abs" style="left:606px;top:370px;transform:rotate(-90deg);transform-origin:left top;font-size:13px;letter-spacing:2px;color:rgba(255,255,255,.8)">TRESSERA Midtown</div>
<div class="photo" role="img" aria-label="Stylist's hands sectioning hair with a comb" style="left:634px;top:70px;width:566px;height:444px;background:linear-gradient(135deg,#7a6a5e,#3c3531 55%,#24201e)"></div>
<div class="abs" style="left:700px;top:370px;font-family:'Poppins',sans-serif;font-size:130px;font-weight:300;letter-spacing:4px;color:rgba(255,255,255,.08);white-space:nowrap">TRESSERA</div>
<div class="abs" style="left:670px;top:220px;width:95px;height:2px;background:var(--white)"></div>
<div class="abs" style="left:679px;top:235px;font-size:13px;letter-spacing:4px;color:var(--white)">BRIDAL &amp; SPECIAL OCCASION</div>
<div class="abs serif" style="left:725px;top:244px;font-size:38px;font-weight:700;color:var(--white);letter-spacing:1px">HAIRSTYLES</div>
<div class="btn btn-yellow" style="left:768px;top:310px;width:187px;height:42px">Make an appointment</div>

<!-- ABOUT -->
<div class="abs" style="left:244px;top:637px"><div class="h-serif">Awesome Things</div><div class="h-sub">About TRESSERA!</div></div>
<p class="abs small" style="left:244px;top:698px;width:350px">At Tressera Midtown, our goal is to provide each of our clients with the <b style="color:var(--ink)">best customer service a salon</b> can offer. In doing so, we ask that our clients give us a 24-hour notice for cancelling their appointment.</p>
<p class="abs small" style="left:244px;top:752px">Thank you for your understanding.</p>
<div class="btn btn-orange" style="left:244px;top:795px;width:149px;height:43px">Contact now</div>
<svg class="abs" style="left:773px;top:563px" width="115" height="128" viewBox="0 0 115 128"><polygon points="0,0 115,12 20,128" fill="#fcc62a"/></svg>
<div class="photo" role="img" aria-label="Woman with long blonde curly hair" style="left:775px;top:590px;width:425px;height:325px;background:linear-gradient(120deg,#f4efe9,#e8cfae 50%,#f6f1ea)"></div>
<div class="photo" role="img" aria-label="Hair close-up in warm orange tones" style="left:609px;top:631px;width:183px;height:203px;background:linear-gradient(160deg,#f0a34e,#d98a33 50%,#f3b362)"></div>

<!-- LATEST TRENDS -->
<div class="abs" style="left:0;top:960px;width:1200px;height:375px;background:var(--orange)"></div>
<div class="abs" style="left:317px;top:1038px;width:562px;height:400px;background:var(--white);box-shadow:0 6px 20px rgba(0,0,0,.1)"></div>
<div class="abs serif" style="left:357px;top:1010px;font-size:82px;font-weight:900;line-height:90px">Latest</div>
<div class="abs" style="left:480px;top:1098px;font-size:28px;font-weight:400">Trends.</div>
<div class="photo" role="img" aria-label="Barber trimming a man's dark hair with scissors" style="left:355px;top:1144px;width:488px;height:191px;background:linear-gradient(100deg,#3a3430,#7d6f66 45%,#dcd6d2)"></div>
<div class="abs" style="left:355px;top:1352px"><div class="h-serif">Awesome Things</div><div class="h-sub">About TRESSERA!</div></div>
<p class="abs small" style="left:355px;top:1400px;width:270px;font-size:8px;line-height:10px">Midtown Harbor Falls offers meter parking. We recommend the city parking ramp that is on the corner of Cedar and Birch.</p>
<div class="btn btn-yellow" style="left:655px;top:1367px;width:188px;height:43px">Make an appointment</div>

<!-- OUR STYLES -->
<div class="abs" style="left:0;top:1492px;width:1200px;text-align:center;font-size:28px"><span class="serif" style="font-weight:700">Our</span> Styles!</div>
<p class="abs small" style="left:440px;top:1537px;width:320px;text-align:center">Our team is dedicated to the highest level of quality and professionalism, all in a comfortable and relaxing atmosphere.</p>
<div class="abs grid">
  <div role="img" aria-label="Back of a man's fade haircut with a design" style="background:linear-gradient(160deg,#c9a892,#5a4a44)"></div>
  <div class="cell" style="background:var(--cream)"><h3>Men Hair</h3><div class="kind">Style</div><div class="at">@ Tressera Midtown</div><div class="price">$650.00</div></div>
  <div role="img" aria-label="Woman's long wavy highlighted hair from behind" style="background:linear-gradient(160deg,#8a7a6e,#c8a57c 55%,#e7d3b5)"></div>
  <div class="cell" style="background:var(--mint)"><h3>Women Hair</h3><div class="kind">Style</div><div class="at">@ Tressera Midtown</div><div class="price">$1,050.00</div></div>
  <div class="cell" style="background:var(--blush)"><h3>Men Hair</h3><div class="kind">Style</div><div class="at">@ Tressera Midtown</div><div class="price">$850.00</div></div>
  <div role="img" aria-label="Man in a salon cape after a haircut" style="background:linear-gradient(160deg,#6d5d55,#c7a08a 50%,#2c2a2a)"></div>
  <div class="cell" style="background:var(--ice)"><h3>Bridal</h3><div class="kind">Hair &amp; Nail Styles</div><div class="at">@ Tressera Midtown</div><div class="price">$3,250.00</div></div>
  <div role="img" aria-label="Woman's hand with manicured nails touching an earring" style="background:linear-gradient(160deg,#f1e7e2,#d9b7a7 55%,#efe4de)"></div>
</div>
<div class="btn btn-orange" style="left:525px;top:2003px;width:149px;height:43px">View all styles</div>

<!-- HAIR SERUMS -->
<div class="photo" role="img" aria-label="Stylist cutting a client's long dark hair" style="left:0;top:2095px;width:472px;height:652px;background:linear-gradient(150deg,#d8cbbf,#8a6a58 45%,#4a3a33 70%,#bdb2aa)"></div>
<div class="abs" style="left:377px;top:2235px;width:306px;height:372px;background:var(--grey-bg)"></div>
<div class="abs" style="left:230px;top:2270px;font-size:130px;font-weight:300;color:rgba(0,0,0,.07);white-space:nowrap">TRESSERA</div>
<div class="abs" style="left:393px;top:2248px;font-size:9px;letter-spacing:2px;color:var(--text)">MEN &amp; WOMEN</div>
<div class="abs serif" style="left:393px;top:2258px;font-size:29px;font-weight:700">Hair Serums</div>
<div class="photo" role="img" aria-label="Row of blue hair serum bottles" style="left:437px;top:2390px;width:246px;height:217px;background:linear-gradient(180deg,#f4f4f4 10%,#2c4a7a 40%,#1c3359)"></div>
<div class="abs" style="left:655px;top:2208px;width:310px;height:216px;background:var(--white);box-shadow:0 4px 18px rgba(0,0,0,.08)"></div>
<div class="abs" style="left:686px;top:2246px"><div class="h-serif">Awesome Things</div><div class="h-sub">About TRESSERA!</div></div>
<p class="abs small" style="left:686px;top:2298px;width:260px;font-size:8px;line-height:13px">Midtown Harbor Falls offers meter parking. We recommend the city parking ramp that is on the corner of Cedar and Birch.</p>
<p class="abs small" style="left:686px;top:2343px;width:260px;font-size:8px;line-height:13px">Our team is dedicated to the highest level of quality and professionalism, all in a comfortable and relaxing atmosphere.</p>
<div class="btn btn-yellow" style="left:683px;top:2399px;width:185px;height:43px">Make an appointment</div>

<!-- SERVICES -->
<div class="svc" style="left:225px">
  <div class="ring"><svg width="44" height="44" viewBox="0 0 44 44" fill="none" stroke="#1c1c1c" stroke-width="1.5"><circle cx="10" cy="34" r="5"/><circle cx="34" cy="34" r="5"/><path d="M14 30 36 6M30 30 8 6"/></svg></div>
  <div class="slash">//</div><h4>Hair Style</h4>
</div>
<div class="svc" style="left:420px">
  <div class="ring fill"><svg width="44" height="44" viewBox="0 0 44 44" fill="none" stroke="#fff" stroke-width="1.5"><circle cx="22" cy="18" r="11"/><path d="M14 40c0-6 4-9 8-9s8 3 8 9"/></svg></div>
  <div class="slash">//</div><h4>Make Up</h4>
  <p class="small" style="font-size:8px;line-height:15px;margin-top:12px">Our team is dedicated to the highest level of quality and professionalism, all in a comfortable and relaxing atmosphere.</p>
</div>
<div class="svc" style="left:620px">
  <div class="ring"><svg width="44" height="44" viewBox="0 0 44 44" fill="none" stroke="#1c1c1c" stroke-width="1.5"><rect x="12" y="28" width="6" height="12"/><path d="M15 28V12l10-6 8 14-8 4"/></svg></div>
  <div class="slash">//</div><h4>Nails Design</h4>
</div>
<div class="svc" style="left:815px">
  <div class="ring"><svg width="44" height="44" viewBox="0 0 44 44" fill="none" stroke="#1c1c1c" stroke-width="1.5"><rect x="8" y="14" width="30" height="12" rx="3" transform="rotate(-35 22 22)"/><path d="M14 30l-4 4M18 33l-3 4M22 36l-3 4"/></svg></div>
  <div class="slash">//</div><h4>Specials</h4>
</div>

<!-- SOCIAL FEED -->
<div class="abs" style="left:75px;top:3083px;width:1125px;height:287px;background:var(--grey-bg)"></div>
<div class="abs" style="left:287px;top:3117px;width:13px;height:13px;border:2px solid var(--orange);border-radius:3px"></div>
<div class="abs" style="left:806px;top:3117px;font-size:11px;color:var(--text)">@tresseramidtown/</div>
<div class="photo" role="img" aria-label="Stylist combing a client's long hair" style="left:287px;top:3148px;width:209px;height:192px;background:linear-gradient(150deg,#cfc3b8,#6e5346 55%,#3c302b)"></div>
<div class="photo" role="img" aria-label="Smiling client after a haircut" style="left:496px;top:3148px;width:209px;height:192px;background:linear-gradient(160deg,#f7b25a,#f09a3e 60%,#e68a32)"></div>
<div class="abs" style="left:530px;top:3235px;width:140px;text-align:center;font-size:8px;color:var(--white);opacity:.85">Just some fresh styles... tap to see more</div>
<div class="photo" role="img" aria-label="Barber shaping a man's hair with a comb" style="left:705px;top:3148px;width:208px;height:192px;background:linear-gradient(150deg,#b2a296,#6a4a3a 55%,#e0d6cf)"></div>

<!-- FOOTER -->
<div class="abs f-head" style="left:234px;top:3407px">Hours<br>Of Operation</div>
<table class="abs hours" style="left:234px;top:3452px;border-collapse:collapse">
<tr><td>Monday</td><td>10 am-7 pm</td></tr><tr><td>Tuesday</td><td>9 am-7 pm</td></tr><tr><td>Wednesday</td><td>10 am-7 pm</td></tr><tr><td>Thursday</td><td>9 am-7 pm</td></tr><tr><td>Friday</td><td>9 am-8 pm</td></tr><tr><td>Saturday</td><td>10 am-3 pm</td></tr><tr><td>Sunday</td><td>Closed</td></tr>
</table>
<div class="abs f-head" style="left:466px;top:3407px">Contact<br>Information</div>
<div class="abs" style="left:466px;top:3456px;font-size:7px;line-height:9px;color:var(--text)">418 Cedar Lane<br>Suite 3<br><br>Harbor Falls,<br>MI 49010</div>
<svg class="abs" style="left:555px;top:3468px" width="24" height="24" viewBox="0 0 24 24"><path d="M5 3l4 0 2 5-3 2c1 3 3 5 6 6l2-3 5 2v4c0 1-1 2-2 2C10 21 3 14 3 5c0-1 1-2 2-2z" fill="none" stroke="#1c1c1c" stroke-width="1.5"/></svg>
<div class="abs serif" style="left:585px;top:3470px;font-size:17px;color:var(--orange)">555 - 014 - 2290</div>
<div class="abs" style="left:540px;top:3545px;display:flex;align-items:center;gap:8px"><span class="brand-mark"></span><span class="brand-name" style="font-size:20px">TRESSERA</span></div>
<div class="abs f-head" style="left:793px;top:3407px">About<br>Tressera Midtown</div>
<p class="abs" style="left:793px;top:3450px;width:170px;font-size:7px;line-height:9px;color:var(--text)">At Tressera Midtown we are committed to providing an unparalleled experience using only the most advanced and innovative techniques to achieve classic and contemporary styles for our clients in the heart of Midtown Harbor Falls.</p>
<p class="abs" style="left:793px;top:3520px;width:170px;font-size:7px;line-height:9px;color:var(--text)">Our team is dedicated to the highest level of quality and professionalism, all in a comfortable and relaxing atmosphere.</p>
<div class="abs" style="left:234px;top:3630px;width:732px;height:1px;background:var(--line)"></div>
<div class="abs" style="left:0;top:3641px;width:1200px;text-align:center;font-size:7px;color:var(--text)">Tressera Midtown • Harbor Falls • Midtown • Haircut • Color • Nails • Manicures • Pedicures • Waxing • Mens Services • Bridal • Best</div>
<div class="abs" style="left:0;top:3658px;width:1200px;text-align:center;font-size:7px;color:var(--text)">© 2014 - 2019 <b style="color:var(--ink)">Tressera Midtown</b>. All rights reserved.</div>
<div class="abs" style="left:0;top:3668px;width:1200px;text-align:center;font-size:7px;color:var(--text)">Terms / Privacy</div>

</body>
</html>
```